Building Design company needing a letterhead

We need a letter head for our Building Design company to send letters etc. to our clients, consultants, councils etc. We would like to see our logo used and company colours. I have attached our style guide and an example of our current letterheads. Top left we would like our logo, top right we would like the company details and at the footer we would like some sort of image/design etc. that suits our brand. I like the Quarto Design letterhead attached.

Target Market(s)

Professionals, Councils, Consultants, Mums & Dads

Industry/Entity Type

Architecture

Font styles to use
Other font styles liked:
• refer the design style guide

Colors
f37122
000000
1b1b1b

Requirements
Must have
• Must have the minimum of a logo, company details and footer
Nice to have
• An image/design made for the footer that would suite our brand and website at www.tavorendesign.com.au. Also it would be nice to include the KMOTR logo somewhere perhaps included in the footer.
Should not have
• Large images in the header. I just want the logo and company details.

```html
<!DOCTYPE html>
<html lang="en">
<head>
<meta charset="utf-8">
<title>Tavoren Design — Letterhead</title>
<link href="https://fonts.googleapis.com/css2?family=Arimo:wght@400;700&display=swap" rel="stylesheet">
<style>
  :root {
    --backdrop: #5c4b42;
    --paper: #ffffff;
    --brand-orange: #f37122;
    --ink: #1b1b1b;
    --ink-soft: #3a3a3a;
    --rule: #555555;
  }
  * { margin: 0; padding: 0; box-sizing: border-box; }
  html, body {
    width: 967px; height: 1200px; overflow: hidden;
    background: var(--backdrop);
    font-family: "Arimo", Arial, sans-serif;
  }
  .letterhead {
    position: absolute; left: 135px; top: 133px;
    width: 720px; height: 932px;
    background: var(--paper);
  }
  .brand {
    position: absolute; left: 231px; top: 55px;
    display: flex; align-items: center; gap: 14px;
  }
  .brand-square {
    width: 60px; height: 60px; background: var(--brand-orange);
  }
  .brand-name {
    color: var(--ink); font-weight: 700; font-size: 32px;
    line-height: 34px; letter-spacing: 2px;
  }
  .footer {
    position: absolute; left: 35px; top: 873px;
    font-size: 11.5px; line-height: 16.5px; color: var(--ink-soft);
  }
  .footer-col { position: absolute; top: 0; white-space: nowrap; }
  .footer-address { left: 0; }
  .footer-contact { left: 256px; color: var(--brand-orange); font-weight: 700; }
  .footer-web { left: 416px; }
  .footer-divider {
    position: absolute; top: -3px; width: 1px; height: 28px; background: var(--rule);
  }
  .divider-one { left: 238px; }
  .divider-two { left: 397px; }
  .partner-badge {
    position: absolute; left: 620px; top: 835px;
    width: 53px; height: 54px; border: 2px solid var(--brand-orange);
  }
</style>
</head>
<body>
  <main class="letterhead">
    <header class="brand">
      <div class="brand-square"></div>
      <div class="brand-name">TAVOREN<br>DESIGN</div>
    </header>

    <footer class="footer">
      <div class="footer-col footer-address">
        Unit 3/22 Harbour Way Seaview WA 6300<br>
        PO Box 5187 Seaview North WA 6300
      </div>
      <span class="footer-divider divider-one"></span>
      <div class="footer-col footer-contact">
        PHONE (08) 6123 4470<br>
        ABN 41 782 306 914
      </div>
      <span class="footer-divider divider-two"></span>
      <div class="footer-col footer-web">
        admin@tavorendesign.com.au<br>
        www.tavorendesign.com.au
      </div>
    </footer>
    <div class="partner-badge" role="img" aria-label="Partner association badge"></div>
  </main>
</body>
</html>
```